$$$ F&B Needs New Theme for its takeaway bowls, Cups and Theme!

Hi everyone,
J here, representing 东岭米糕 donglingmigao, a soy based f&b company situated in China, selling delicious tofu pudding, soy beverages and simple bites.
东岭米糕 is currently looking to revamp its current set of bowls and cups and materials and we would love to receive your input on this!
We are looking for a theme and concept to print onto our:
1) disposable large sized plastic bowl model: P360
Printable Area: 2.5cm tall by 32cm of circumference
2) disposable 16oz plastic cup model: H500B
Printable Area 1 : 8cm tall by 22cm of circumference
Printable Area 2: 9cm tall by 20cm of circumference
3) paper bag/box to wrap our pies in size:
Printable Area: height 11cm by breadth 9cm by thickness 4.5cm
Please restrict to using 4 colours max.
The below links point to some themes we especially like:
1)
http://www.plumorex-sample.com.tw/portfolio-item-one/
2)
http://www.plumorex-sample.com.tw/portfolio-item-two/
3)
http://www.plumorex-sample.com.tw/portfolio-item-three/
as you can see, we would like an oriental/ asian/ chinese feel, with things like wood, white, red stamps, brown paper, calligraphy and things like that.
it would help if you could mock up your design on to a disposable bowl to show us.
here is the info you should also display
1) our logo.
2) the text "donglingmigao"
3) www.donglingmigao-shop.com
4) 微信号: dlmg6262
5) 微博:东岭米糕
6) 加盟热线:186 2719 4053
we are an existing business with some photos at this link to help you better visualize what we want.
i also uploaded some nanyang chinatown street photos and and sketched street photo... going along the line of antique china/chinese streets feel..
http://www.donglingmigao-shop.com/
Updates
Hi all!
we have up-ed our budget and provided more information on the printable area so it is easier for you to work with.
we are looking to improve our positioning and packaging so pls submit a new design and not a small modification of our current bowl.
please look at the links we have provided, they serve to give you a good idea of what we like.
j
Reason: as requested. waiting for better designs!
Reason: I looking for sketches of chinese streets as background, with 2-3 colours for the sketches.
Not looking into using photos for the packaging.
Reason: for edits

```html
<!DOCTYPE html>
<html lang="zh">
<head>
<meta charset="utf-8">
<title>东岭米糕 Label</title>
<link rel="stylesheet" href="https://fonts.googleapis.com/css2?family=Fredoka:wght@500;600;700&family=Noto+Sans+SC:wght@500&family=ZCOOL+KuaiLe&display=swap">
<style>
  :root {
    --page: #ffffff;
    --bean-dark: #2f1e0c;
    --bean-tan: #c9a866;
    --bean-light: #ddc287;
    --bean-pale: #e3ca92;
    --bean-deep: #9a7232;
    --bean-shadow: #7d5a22;
    --cream: #f2e68c;
    --cream-text: #f3e48a;
    --ink: #3a2510;
    --seal: #a50f1c;
  }
  * { margin: 0; padding: 0; box-sizing: border-box; }
  html, body { width: 1200px; height: 1000px; overflow: hidden; background: var(--page); }
  .label {
    position: absolute; left: 284px; top: 264px;
    width: 611px; height: 408px;
    background: var(--bean-dark);
    font-family: "Fredoka", "Noto Sans SC", sans-serif;
    overflow: hidden;
  }
  .top-band { position: absolute; left: 0; top: 0; width: 100%; height: 45px; background: var(--bean-dark); }
  .bean-field {
    position: absolute; left: 0; top: 45px; width: 100%; height: 179px;
    background:
      radial-gradient(ellipse 90px 60px at 8% 30%, var(--bean-pale), transparent 70%),
      radial-gradient(ellipse 110px 70px at 28% 55%, var(--bean-light), transparent 70%),
      radial-gradient(ellipse 100px 60px at 50% 25%, var(--bean-pale), transparent 70%),
      radial-gradient(ellipse 120px 70px at 70% 60%, var(--bean-light), transparent 70%),
      radial-gradient(ellipse 90px 60px at 90% 30%, var(--bean-pale), transparent 70%),
      radial-gradient(ellipse 80px 50px at 18% 90%, var(--bean-deep), transparent 70%),
      radial-gradient(ellipse 80px 50px at 62% 95%, var(--bean-deep), transparent 70%),
      radial-gradient(ellipse 70px 40px at 40% 5%, var(--bean-deep), transparent 70%),
      linear-gradient(180deg, var(--bean-tan), var(--bean-tan) 70%, var(--bean-shadow));
  }
  .brand-band { position: absolute; left: 0; top: 224px; width: 100%; height: 139px; background: var(--bean-dark); }
  .brand-name {
    position: absolute; left: 148px; top: 12px;
    font-family: "ZCOOL KuaiLe", sans-serif;
    font-size: 72px; line-height: 80px; letter-spacing: 8px;
    color: var(--cream-text);
  }
  .brand-seal {
    position: absolute; left: 453px; top: 3px;
    width: 26px; height: 56px; border-radius: 6px;
    background: var(--seal);
  }
  .brand-roman {
    position: absolute; left: 186px; width: 220px; top: 94px;
    text-align: center;
    font-family: "Fredoka", sans-serif;
    font-weight: 700; font-size: 22px; line-height: 26px; letter-spacing: -0.3px;
    color: var(--cream-text);
  }
  .social {
    position: absolute; top: 110px;
    font-family: "Noto Sans SC", "Fredoka", sans-serif;
    font-weight: 500; font-size: 14px; line-height: 18px;
    color: var(--cream-text);
  }
  .social--wechat { left: 14px; }
  .social--weibo { right: 14px; }
  .contact-band {
    position: absolute; left: 0; top: 363px; width: 100%; height: 45px;
    background: var(--cream);
    display: flex; align-items: center; justify-content: space-between;
    padding: 0 21px;
    font-weight: 600; font-size: 15px; color: var(--ink);
  }
</style>
</head>
<body>
  <div class="label">
    <div class="top-band"></div>
    <div class="bean-field" role="img" aria-label="Close-up illustration of golden soybeans"></div>
    <div class="brand-band">
      <div class="brand-name">东岭米糕</div>
      <div class="brand-seal"></div>
      <div class="brand-roman">donglingmigao</div>
      <div class="social social--wechat">微信号： dlmg6262</div>
      <div class="social social--weibo">微博:东岭米糕</div>
    </div>
    <div class="contact-band">
      <span class="contact-web">www.donglingmigao-shop.com</span>
      <span class="contact-phone">Hotline： 186 2719 4053</span>
    </div>
  </div>
</body>
</html>
```